New Attorney in Non-Traditional Field Needs Creative Edgy Legal Business Card with Side Business Not

I need a new personal business card. Away from the silver lettering on heavy white card stock, Velvet Harbor anyone? I'm newly admitted to the CA bar, I started my own small side-business in sales, I'm arbitrating on a part time basis, and I'm creating a ViewCast channel about current news from young professionals' perspective in January. On the side I've been taking a lot of home buying negotiation classes, and I do a lot of yoga. It would be my dream job to advise clients in the startup/entrepreneurial world. I would like my Viewcast channel, website (www.marlowbead.example/ninaprell), phone number, email, admittance #, and link for workweb featured on my card. The colors and message of homepage www.calmheronflow.example really speak to me. Often I'll read that Mavis Token quote about doing one thing for your brand everyday, and I believe it in wholeheartedly.
Updates

Perrin's design has been accepted with very minimal changes. Thank you all for your submissions. This has been a fun experience.

Target Market(s)

all young attorneys, small startups, small tech, potential employers, networking events for lawyers and other young professionals

Industry/Entity Type

Business

Contact Information for Business Card

Rosalind K. Prell, Esq.
Attorney bar card number
Ph (555) 482-7716
Email Nina.Prell@mailbox.example
Work web website
Viewcast Channel coming soon!
Marlow & Bead website

Font styles to use
Sans Serif
Decorative

Requirements
Must have
• A simple image or logo that can transition to other products as I build my brand. Great colors. Maybe all white & gold? Maybe a cool blues/purples motif?

```html
<!DOCTYPE html>
<html lang="en">
<head>
<meta charset="utf-8">
<title>Rosalind K. Prell — Business Card</title>
<link rel="stylesheet" href="https://fonts.googleapis.com/css2?family=Alex+Brush&family=Crimson+Text:wght@400&display=swap">
<style>
  :root {
    --page-bg: #ffffff;
    --card-bg: #5e5c5f;
    --card-bg-light: #69676a;
    --frame-gold: #dcb23a;
    --text-gold: #e6c23c;
    --name-gold-light: #f6e27a;
    --name-gold-mid: #e3b928;
    --name-gold-dark: #b8860f;
    --mark-orange: #e8622a;
  }
  * { margin: 0; padding: 0; box-sizing: border-box; }
  html, body {
    width: 1200px;
    height: 702px;
    overflow: hidden;
    background: var(--page-bg);
  }
  .canvas {
    position: relative;
    width: 1200px;
    height: 702px;
  }
  .business-card {
    position: absolute;
    left: 40px;
    top: 38px;
    width: 1124px;
    height: 626px;
    border: 5px solid var(--frame-gold);
    border-radius: 7px;
    background: radial-gradient(ellipse at 50% 45%, var(--card-bg-light) 0%, var(--card-bg) 75%);
  }
  .brand-mark {
    position: absolute;
    left: 0;
    right: 0;
    top: 178px;
    display: flex;
    justify-content: center;
    align-items: center;
    gap: 10px;
    font-family: "Crimson Text", Georgia, serif;
    font-size: 26px;
    color: var(--mark-orange);
    letter-spacing: 2px;
  }
  .brand-mark__dot {
    width: 14px;
    height: 14px;
    border-radius: 50%;
    background: var(--mark-orange);
  }
  .holder-name {
    position: absolute;
    left: -30px;
    right: 0;
    top: 270px;
    text-align: center;
    font-family: "Alex Brush", cursive;
    font-size: 116px;
    line-height: 1;
    background: linear-gradient(180deg, var(--name-gold-light) 0%, var(--name-gold-mid) 50%, var(--name-gold-dark) 100%);
    -webkit-background-clip: text;
    background-clip: text;
    color: transparent;
    filter: drop-shadow(3px 4px 2px rgba(0, 0, 0, 0.55));
  }
  .contact {
    position: absolute;
    left: 0;
    right: 0;
    top: 442px;
    text-align: center;
    font-family: "Crimson Text", Georgia, serif;
    font-size: 24px;
    line-height: 36px;
    letter-spacing: -0.6px;
    color: var(--text-gold);
  }
</style>
</head>
<body>
  <main class="canvas">
    <section class="business-card">
      <div class="brand-mark">
        <span class="brand-mark__dot"></span>
        <span class="brand-mark__name">RKP</span>
      </div>
      <h1 class="holder-name">Rosalind K. Prell</h1>
      <div class="contact">
        <p class="contact__line">Esq. Attorney bar card number Ph (555) 482-7716</p>
        <p class="contact__line">Email Nina.Prell@mailbox.example</p>
      </div>
    </section>
  </main>
</body>
</html>
```